Design a poster for Ellery's Dash 2023. A charity event supporting paediatric brain cancer.

We need a new poster for our event in 2023. The successful applicant will have opportunity for ongoing work with our foundation as we need a number of other deliverables once the design is finalised. We have a strong, fun and youthful brand.
Please see attached PDF showing the last 10 years of designs.
Please see attached moodboards outlining concepts for our 2023 theme. The last image of skateboarder concept is "Dusky Glow" - A retro miami vibe Juxtaposed with photo of someone from one of our previous events. Potentially posters could have multiple variants building on lots of different photos.
I have attached our brand guidelines as well as lock ups for our Ellery's Dash logos.
Whatever is created needs to be transferrable on to a number of different mediums, most importantly T-shirts, Web Banners, Billboards, Pavement Stickers, Social posts.
Our sponsor logos will remain the same.
Please only send complete designs - aligned with one of the 4 concepts provided and include all copy as per attached and include sponsors logos. Please ensure the body fonts are Brandon Grotesque and CCMatinee Idol.
Updates
Hi All, Thank you so much for all the submissions. Unfortunately after our CEO and team have reviewed the designs they are looking to go in quite a different direction than the original brief provided. I apologise for wasting your time. I have updated brief, and more specific moodboards, the last image concept is "Dusky Glow" - A retro miami vibe Juxtaposed with photo of someone from one of our previous events. Potentially posters could have multiple variants building on lots of different photos . If you would like to submit another design that would be great but if not we completely understand. Thank you again for your creative submissions.
Target Market(s)
18-35 year olds
Industry/Entity Type
Not for Profit - Fun Run Event and Party
Font styles to use
Other font styles liked:
- Fonts in Brand Guidelines - Brandon Grotesque and CCMatinee Idol
Requirements
Must have
- On Brand - colourful, focus on ALL SMILES NO MILES

```html
<!DOCTYPE html>
<html lang="en">
<head>
<meta charset="utf-8">
<title>Ellery's Dash 2023 – Poster</title>
<link rel="stylesheet" href="https://fonts.googleapis.com/css2?family=Alfa+Slab+One&family=Bebas+Neue&family=Great+Vibes&family=Jost:wght@300;400;500;600;700&display=swap">
<style>
  :root {
    --cream: #fdf7f0;
    --sand: #f4e9d2;
    --teal: #6ccacb;
    --navy: #1a1f4a;
    --coral: #f59a85;
    --orange: #f7941d;
    --sun: #fdc04f;
    --sans: "Jost", "Helvetica Neue", Arial, sans-serif;
    --script: "Great Vibes", cursive;
    --display: "Alfa Slab One", Georgia, serif;
    --condensed: "Bebas Neue", Impact, sans-serif;
  }
  * { box-sizing: border-box; margin: 0; padding: 0; }
  html, body { width: 848px; height: 1200px; overflow: hidden; background: var(--cream); }
  .poster { position: relative; width: 848px; height: 1200px; overflow: hidden; background: var(--cream); color: var(--navy); font-family: var(--sans); }
  .backdrop { position: absolute; inset: 0; }
  .copy { position: absolute; left: 0; width: 100%; text-align: center; }
  .cause-line { top: 166px; font-size: 27px; font-weight: 300; letter-spacing: 1.5px; }
  .cause-stat { top: 206px; font-size: 26px; font-weight: 500; letter-spacing: 2px; }
  .title { position: absolute; left: 0; top: 0; width: 848px; height: 560px; }
  .event-line { font-size: 34px; font-weight: 500; letter-spacing: 2.5px; line-height: 1; }
  .event-line .script { font-family: var(--script); font-size: 44px; letter-spacing: 0; font-weight: 400; }
  .event-date { font-size: 37px; font-weight: 700; letter-spacing: 2px; line-height: 1; }
  .event-date sup { font-size: 20px; vertical-align: 14px; font-weight: 600; margin-right: 4px; }
  .fun-run { top: 566px; }
  .fun-run-date { top: 620px; }
  .your-way { top: 696px; }
  .your-way-date { top: 740px; }
  .register { top: 852px; font-size: 27px; font-weight: 500; letter-spacing: 2.5px; }
  .ribbon { position: absolute; left: 236px; top: 893px; width: 376px; height: 50px; }
  .ribbon-text { position: absolute; left: 236px; top: 893px; width: 376px; height: 50px; line-height: 52px; text-align: center; font-size: 29px; font-weight: 600; letter-spacing: 2.5px; color: #111; }
  .supporters-label { top: 988px; font-size: 22px; font-weight: 300; letter-spacing: 4px; }
  .sponsor { position: absolute; font-family: var(--sans); font-weight: 600; font-size: 15px; color: var(--navy); display: flex; align-items: center; gap: 5px; transform: translate(-50%, -50%); white-space: nowrap; }
  .sponsor .mark { width: 10px; height: 10px; border-radius: 50%; background: var(--navy); }
  .sponsor-cloudlane { left: 342px; top: 1060px; }
  .sponsor-grocera { left: 436px; top: 1060px; }
  .sponsor-kazumi { left: 524px; top: 1060px; }
  .sponsor-ivy { left: 369px; top: 1123px; }
  .sponsor-signal { left: 471px; top: 1123px; }
  .foundation { position: absolute; left: 628px; top: 982px; width: 194px; height: 194px; border-radius: 50%; background: var(--navy); display: flex; align-items: center; justify-content: center; text-align: center; color: var(--cream); font-family: var(--sans); font-weight: 600; font-size: 20px; letter-spacing: 1.5px; line-height: 1.25; }
</style>
</head>
<body>
<main class="poster">
  <svg class="backdrop" width="848" height="1200" viewBox="0 0 848 1200">
    <path class="backdrop-sand" fill="var(--sand)" d="M92 52 C260 36 560 40 720 48 C790 52 800 90 796 160 C790 300 812 420 800 560 C790 700 806 860 800 1000 C796 1100 780 1180 760 1200 L90 1200 C76 1100 64 980 60 860 C56 720 74 600 58 480 C46 360 52 200 60 110 C64 70 74 56 92 52 Z"/>
    <circle class="backdrop-circle" cx="424" cy="546" r="293" fill="var(--cream)"/>
    <path role="img" aria-label="Teal palm frond illustration" fill="var(--teal)" d="M0 0 L236 0 C226 60 200 120 160 170 C120 220 60 250 12 262 L0 262 Z"/>
    <path role="img" aria-label="Teal monstera leaf illustration" fill="var(--teal)" d="M543 0 L848 0 L848 60 C830 120 800 170 760 190 C720 208 660 200 630 160 C600 130 560 90 543 40 Z"/>
    <ellipse role="img" aria-label="Yellow leaf illustration" cx="400" cy="34" rx="22" ry="40" fill="var(--sun)" transform="rotate(35 400 34)"/>
    <circle role="img" aria-label="Teal pomegranate illustration" cx="79" cy="327" r="26" fill="var(--teal)"/>
    <circle role="img" aria-label="Teal pomegranate illustration" cx="771" cy="914" r="26" fill="var(--teal)"/>
    <circle role="img" aria-label="Teal pomegranate illustration" cx="264" cy="1180" r="26" fill="var(--teal)"/>
    <circle role="img" aria-label="Coral dot" cx="35" cy="404" r="15" fill="var(--coral)"/>
    <circle role="img" aria-label="Coral dot" cx="492" cy="22" r="17" fill="var(--coral)"/>
    <circle role="img" aria-label="Coral dot" cx="160" cy="1036" r="16" fill="var(--coral)"/>
    <circle role="img" aria-label="Yellow dot" cx="762" cy="248" r="14" fill="var(--sun)"/>
    <circle role="img" aria-label="Coral sun circle" cx="820" cy="342" r="50" fill="var(--coral)"/>
    <ellipse role="img" aria-label="Orange confetti dot pattern" cx="800" cy="560" rx="48" ry="200" fill="var(--orange)" opacity="0.35"/>
    <path role="img" aria-label="Coral concentric rings illustration" fill="var(--coral)" d="M0 637 C60 650 102 700 102 770 C102 840 60 890 0 900 Z"/>
    <path role="img" aria-label="Teal sun with navy rays illustration" fill="var(--teal)" d="M0 1020 C80 1020 160 1090 167 1200 L0 1200 Z"/>
    <ellipse role="img" aria-label="Navy outline pebbles illustration" cx="46" cy="522" rx="36" ry="36" fill="var(--navy)" opacity="0.12"/>
    <ellipse role="img" aria-label="Navy outline pebbles illustration" cx="808" cy="812" rx="38" ry="36" fill="var(--navy)" opacity="0.12"/>
    <ellipse role="img" aria-label="Navy outline pebbles illustration" cx="300" cy="30" rx="34" ry="30" fill="var(--navy)" opacity="0.12"/>
    <ellipse role="img" aria-label="Navy outline pebbles illustration" cx="60" cy="940" rx="20" ry="28" fill="var(--navy)" opacity="0.12"/>
  </svg>

  <p class="copy cause-line">Supporting Mind Forward</p>
  <p class="copy cause-stat">The #1 disease killer of young</p>

  <svg class="title" viewBox="0 0 848 560" role="heading" aria-level="1" aria-label="Ellery's Dash, September 2023">
    <defs>
      <path id="title-arc" d="M190 438 Q424 290 658 438"/>
    </defs>
    <g font-family="Alfa Slab One, Georgia, serif" font-size="64" letter-spacing="6">
      <text fill="var(--navy)" transform="translate(-5 5)"><textPath href="#title-arc" startOffset="50%" text-anchor="middle">ELLERY'S</textPath></text>
      <text fill="var(--teal)"><textPath href="#title-arc" startOffset="50%" text-anchor="middle">ELLERY'S</textPath></text>
    </g>
    <g font-family="Bebas Neue, Impact, sans-serif" font-size="40">
      <text x="263" y="496" textLength="58" lengthAdjust="spacingAndGlyphs" fill="var(--navy)" transform="translate(-2 2)">SEPT</text>
      <text x="263" y="496" textLength="58" lengthAdjust="spacingAndGlyphs" fill="var(--teal)">SEPT</text>
      <text x="529" y="496" textLength="59" lengthAdjust="spacingAndGlyphs" fill="var(--navy)" transform="translate(-2 2)">2023</text>
      <text x="529" y="496" textLength="59" lengthAdjust="spacingAndGlyphs" fill="var(--teal)">2023</text>
    </g>
    <g font-family="Alfa Slab One, Georgia, serif" font-size="84">
      <text x="336" y="510" textLength="180" lengthAdjust="spacingAndGlyphs" fill="var(--navy)" transform="translate(-4 4)">DASH</text>
      <text x="336" y="510" textLength="180" lengthAdjust="spacingAndGlyphs" fill="var(--teal)">DASH</text>
    </g>
  </svg>

  <p class="copy event-line fun-run">Fun <span class="script">Run</span> and <span class="script">Party</span></p>
  <p class="copy event-date fun-run-date">Sunday 10<sup>th</sup>September</p>
  <p class="copy event-line your-way">Your <span class="script">Way</span> Any <span class="script">Day</span></p>
  <p class="copy event-date your-way-date">All of September</p>

  <p class="copy register">Register or support a participant at</p>
  <svg class="ribbon" viewBox="0 0 376 50" aria-hidden="true">
    <polygon points="0,0 376,0 358,25 376,50 0,50 18,25" fill="var(--orange)"/>
  </svg>
  <p class="ribbon-text">ELLERYSDASH.COM</p>

  <p class="copy supporters-label">Proudly supported by:</p>
  <div class="sponsor sponsor-cloudlane"><span class="mark"></span>Cloudlane</div>
  <div class="sponsor sponsor-grocera">Grocera</div>
  <div class="sponsor sponsor-kazumi">Kazumi</div>
  <div class="sponsor sponsor-ivy">Ivy Property</div>
  <div class="sponsor sponsor-signal">Signalwave</div>

  <div class="foundation">Hartwell<br>Foundation</div>
</main>
</body>
</html>
```